Lumora aesthetics offers a range of facial aesthetics treatments by a fully qualified dentist, to a high end crowd. Treatments include antiwrinkle treatment, the use of dermal fillers to provide facial volumisation and rejuvenation and also lip volumisation.
I want a luxurious and bold look. Black background with a bold striking gold logo in the centre possibly incorporating the outline of a face in a subtle yet effective way. I want it to include the work I offer so people will be aware of what they are looking into but not look like there's too much on the card, So it's a clean look.
At the bottom I would like it to say by Dr. Meera Sandhu. Alongside my email address and mobile number.

```html
<!DOCTYPE html>
<html lang="en">
<head>
<meta charset="utf-8">
<title>Lumora aesthetics – business card</title>
<link rel="stylesheet" href="https://fonts.googleapis.com/css2?family=Open+Sans:wght@400;600&display=swap">
<style>
  :root {
    --backdrop: #2a2a2c;
    --card: #1e1e20;
    --card-edge: #3a3b3e;
    --gold: #d2ad37;
    --ink-light: #f2f2f2;
    --ink-soft: #bdbdbd;
  }
  * { box-sizing: border-box; margin: 0; padding: 0; }
  html, body {
    width: 1200px;
    height: 800px;
    overflow: hidden;
    background: var(--backdrop);
    font-family: "Open Sans", "Segoe UI", sans-serif;
  }
  .stage {
    width: 1200px;
    height: 800px;
    display: flex;
    align-items: center;
    justify-content: center;
    gap: 60px;
  }
  .card {
    position: relative;
    width: 520px;
    height: 300px;
    background: var(--card);
    border: 1px solid var(--card-edge);
    border-radius: 18px;
    box-shadow: 0 12px 30px rgba(0, 0, 0, 0.45);
  }
  /* Front */
  .card--front {
    display: flex;
    flex-direction: column;
    align-items: center;
    padding-top: 48px;
  }
  .brand-mark {
    width: 90px;
    height: 90px;
    border-radius: 50%;
    background: var(--gold);
  }
  .brand-name {
    margin-top: 14px;
    color: var(--gold);
    font-size: 28px;
    font-weight: 400;
    letter-spacing: 2px;
    line-height: 1.2;
  }
  .treatments {
    margin-top: 8px;
    color: var(--ink-soft);
    font-size: 12px;
    letter-spacing: 1.5px;
    text-transform: uppercase;
  }
  .byline {
    position: absolute;
    bottom: 22px;
    left: 0;
    right: 0;
    text-align: center;
    color: var(--ink-light);
    font-size: 13px;
    letter-spacing: 1.5px;
  }
  /* Back */
  .contact-row {
    position: absolute;
    top: 70px;
    left: 0;
    right: 0;
    display: flex;
    align-items: center;
    justify-content: center;
    gap: 22px;
  }
  .practitioner {
    color: var(--ink-light);
    font-size: 18px;
    letter-spacing: 2px;
  }
  .divider {
    width: 3px;
    height: 44px;
    background: var(--gold);
  }
  .contact-list {
    list-style: none;
    display: flex;
    flex-direction: column;
    gap: 6px;
  }
  .contact-item {
    display: flex;
    align-items: center;
    gap: 10px;
    color: var(--ink-light);
    font-size: 14px;
    letter-spacing: 1.5px;
  }
  .contact-icon { width: 16px; height: 16px; flex: none; }
  .back-mark {
    position: absolute;
    left: 50%;
    top: 170px;
    width: 84px;
    height: 84px;
    margin-left: -42px;
    border-radius: 50%;
    background: var(--gold);
  }
</style>
</head>
<body>
<main class="stage">
  <section class="card card--front" aria-label="Card front">
    <div class="brand-mark" aria-hidden="true"></div>
    <h1 class="brand-name">Lumora aesthetics</h1>
    <p class="treatments">Anti-wrinkle · Dermal fillers · Lip volumisation</p>
    <p class="byline">by Dr. Meera Sandhu</p>
  </section>

  <section class="card card--back" aria-label="Card back">
    <div class="contact-row">
      <p class="practitioner">Dr. Meera Sandhu</p>
      <span class="divider" aria-hidden="true"></span>
      <ul class="contact-list">
        <li class="contact-item">
          <svg class="contact-icon" viewBox="0 0 16 16" aria-hidden="true">
            <rect x="3.5" y="1" width="9" height="14" rx="1.5" fill="none" stroke="var(--gold)" stroke-width="1.6"/>
            <circle cx="8" cy="12.4" r="0.9" fill="var(--gold)"/>
          </svg>
          00 987 654 321
        </li>
        <li class="contact-item">
          <svg class="contact-icon" viewBox="0 0 16 16" aria-hidden="true">
            <rect x="1" y="3" width="14" height="10" fill="var(--gold)"/>
            <path d="M1 3 L8 9 L15 3" fill="none" stroke="var(--card)" stroke-width="1.2"/>
          </svg>
          hello@lumoraclinic.com
        </li>
      </ul>
    </div>
    <div class="back-mark" aria-hidden="true"></div>
  </section>
</main>
</body>
</html>
```